Flyer-Design für Jungwinzergruppe
Zielgruppe
Wir sind eine Jungwinzergruppe und produzieren unsere eigenen Weine und Sekte. Unsere Zielgruppe ist gemischt aus jungen und älteren Leuten.

```html
<!DOCTYPE html>
<html lang="de">
<head>
<meta charset="utf-8">
<title>Die Jungwinzer – Flyer</title>
<link href="https://fonts.googleapis.com/css2?family=Aldrich&family=Quicksand:wght@400;600&display=swap" rel="stylesheet">
<style>
:root{
  --wine:#9c3f4b;
  --wine-dark:#7e2f3a;
  --paper:#f6f6f6;
  --ink:#6a6a6a;
  --white:#ffffff;
  --stage:#e9e9e9;
  --photo-people:linear-gradient(160deg,#8a8f93,#3d4654 55%,#6d7480);
  --photo-vine:linear-gradient(180deg,#b9c2c6,#6f8a5a 45%,#4d6b37);
  --photo-bottles:linear-gradient(150deg,#d8d2c4,#5b2a2e 45%,#b5a88a);
  --photo-grey:linear-gradient(160deg,#c9c9c9,#5d5d5d);
}
*{margin:0;padding:0;box-sizing:border-box}
html,body{width:1200px;height:2800px;overflow:hidden}
body{background:var(--stage);font-family:"Quicksand",sans-serif;color:var(--ink);position:relative}
.spread{position:absolute;left:30px;width:1140px;height:806px;display:flex;box-shadow:0 12px 40px rgba(0,0,0,.18)}
.spread--outside{top:390px}
.spread--inside{top:1600px}
.panel{position:relative;width:380px;height:806px;overflow:hidden}
.panel--light{background:var(--paper)}
.panel--wine{background:var(--wine);color:var(--white)}
.photo{position:absolute}
.curve{position:absolute;left:0;width:380px}
.heading{font-family:"Aldrich",sans-serif;font-weight:400;display:flex;align-items:center;gap:10px;border-bottom:1px solid currentColor;padding-bottom:6px}
.heading::before{content:"";width:12px;height:12px;border-radius:50%;background:currentColor;flex:none}
.panel--light .heading{color:var(--wine)}
.subline{font-family:"Aldrich",sans-serif;color:var(--wine);font-size:15px;margin:10px 0 8px}
.copy{font-size:11.5px;line-height:1.5;margin-bottom:8px}
.text-block{position:absolute;left:32px;right:32px}

/* cover */
.cover-brand{position:absolute;right:22px;top:150px;display:flex;align-items:center;gap:8px;font-family:"Aldrich",sans-serif;font-size:22px;color:var(--white)}
.cover-brand .mark{width:14px;height:14px;background:var(--white)}
.cover-title{position:absolute;left:30px;right:30px;top:360px;font-family:"Aldrich",sans-serif;text-align:center}
.cover-title h1{font-weight:400;font-size:42px;letter-spacing:1px;border-bottom:1px solid var(--white);padding-bottom:10px}
.cover-title p{font-size:18px;letter-spacing:3px;margin-top:12px}
.cover-url{position:absolute;left:0;right:0;top:735px;text-align:center;font-family:"Aldrich",sans-serif;font-size:17px;color:var(--white)}
.cover-url::after{content:"";display:block;width:120px;height:1px;background:var(--white);margin:8px auto 0}

/* back */
.round-photo{position:absolute;border-radius:50%;border:4px solid var(--white);background:var(--photo-grey)}
.back-brand{position:absolute;left:0;right:0;top:330px;text-align:center;font-family:"Aldrich",sans-serif;font-size:30px;display:flex;justify-content:center;align-items:center;gap:10px}
.back-brand .mark{width:16px;height:16px;background:var(--white)}
.back-heading{position:absolute;left:40px;right:40px;top:470px;font-size:24px}
.back-name{position:absolute;left:50px;top:530px;font-family:"Aldrich",sans-serif;font-size:18px;letter-spacing:2px;line-height:1.15}
.back-name small{display:block;font-size:14px}
.contact{position:absolute;left:50px;top:610px;list-style:none;font-size:12.5px;font-weight:600}
.contact li{display:flex;align-items:center;gap:10px;margin-bottom:12px}
.contact svg{width:14px;height:14px;flex:none}

/* inside middle */
.team-heading{position:absolute;left:40px;right:40px;top:40px;font-size:22px}
.member{position:absolute;left:0;right:0;text-align:center}
.member .round-photo{position:relative;display:block;width:130px;height:130px;margin:0 auto;border-width:3px}
.member p{font-family:"Aldrich",sans-serif;font-size:14px;margin-top:10px}
.member p::after{content:"";display:block;width:90px;height:1px;background:var(--white);margin:6px auto 0}

/* bios */
.bio{position:absolute;left:30px;right:30px}
.bio .heading{font-size:24px;margin-bottom:12px}

.wine-list{list-style:none;font-family:"Aldrich",sans-serif;color:var(--wine);font-size:17px;line-height:1.35}
</style>
</head>
<body>

<!-- Outside: inner flap, back, cover -->
<section class="spread spread--outside">
  <article class="panel panel--light">
    <div class="text-block" style="top:40px">
      <h2 class="heading" style="font-size:24px">Die Jungwinzer</h2>
      <p class="subline">Die neue Lese!</p>
      <p class="copy">Drei junge Winzer, drei verschiedene Philosophien, eine Leidenschaft!</p>
      <p class="copy">2013 gründeten wir, drei Freunde von der Reb, die Jungwinzergruppe, um unsere eigenen Ideen und Vorstellungen in Form eigener Weine zu verwirklichen.</p>
      <p class="copy">Angefangen mit einer kleinen Fläche von rund 700 m² und 500 Flaschen sind wir heute bei einer Fläche von 3000 m² und rund 2800 Flaschen pro Jahr.</p>
      <p class="copy">Durch neue und jüngere Interpretationen des Anbaus und Ausbaus bildete sich unser eigener Stil. Diesen versuchen wir nun weiterzuentwickeln, um einen Wein nach unseren Vorstellungen zu machen. Dabei verbinden wir die Tradition mit frischen Ideen.</p>
    </div>
    <div class="photo" style="left:0;top:560px;width:380px;height:246px;background:var(--photo-people)" role="img" aria-label="Foto: die drei Jungwinzer sitzen mit Weinflaschen auf einer Weinbergsmauer"></div>
    <svg class="curve" style="top:540px" width="380" height="60" viewBox="0 0 380 60" aria-hidden="true">
      <path d="M0 0H380V8Q190 60 0 36Z" fill="var(--paper)"/>
      <path d="M0 36Q190 60 380 8V22Q190 70 0 46Z" fill="var(--wine)"/>
    </svg>
  </article>

  <article class="panel panel--wine">
    <div class="round-photo" style="left:80px;top:30px;width:220px;height:220px" role="img" aria-label="Schwarzweißfoto: die drei Jungwinzer bei der Arbeit im Weinkeller"></div>
    <div class="back-brand"><span class="mark"></span>Rebzeit</div>
    <h2 class="heading back-heading">Ihr Weg zu uns</h2>
    <p class="back-name">Die Jungwinzer<small>die neue Lese</small></p>
    <ul class="contact">
      <li><svg viewBox="0 0 14 14"><path d="M7 1a4 4 0 0 1 4 4c0 3-4 8-4 8S3 8 3 5a4 4 0 0 1 4-4z" fill="var(--white)"/><circle cx="7" cy="5" r="1.5" fill="var(--wine)"/></svg>Talweg 8 | 53400 Rebental</li>
      <li><svg viewBox="0 0 14 14"><rect x="1" y="3" width="12" height="8" fill="var(--white)"/><path d="M1 3l6 5 6-5" stroke="var(--wine)" fill="none"/></svg>hallo@jungwinzer-rebzeit.de</li>
      <li><svg viewBox="0 0 14 14"><circle cx="7" cy="7" r="5.5" fill="var(--white)"/></svg>www.jungwinzer-rebzeit.de</li>
    </ul>
  </article>

  <article class="panel panel--wine">
    <div class="photo" style="left:0;top:0;width:380px;height:320px;background:var(--photo-people)" role="img" aria-label="Foto: die drei Jungwinzer vor einem Weinort"></div>
    <svg class="curve" style="top:270px" width="380" height="60" viewBox="0 0 380 60" aria-hidden="true">
      <path d="M0 60V30Q200 -10 380 40V60Z" fill="var(--wine)"/>
    </svg>
    <div class="cover-brand"><span class="mark"></span>Rebzeit</div>
    <div class="cover-title">
      <h1>Die Jungwinzer</h1>
      <p>Die neue Lese!</p>
    </div>
    <div class="photo" style="left:0;top:560px;width:380px;height:246px;background:var(--photo-vine)" role="img" aria-label="Foto: Weinberge im Herbst über dem Tal"></div>
    <svg class="curve" style="top:540px" width="380" height="60" viewBox="0 0 380 60" aria-hidden="true">
      <path d="M0 0H380V40Q190 0 0 40Z" fill="var(--wine)"/>
      <path d="M0 40Q190 0 380 40V46Q190 8 0 46Z" fill="#4a4a4a"/>
    </svg>
    <p class="cover-url">www.jungwinzer-rebzeit.de</p>
  </article>
</section>

<!-- Inside: wines, team, bios -->
<section class="spread spread--inside">
  <article class="panel panel--light">
    <div class="photo" style="left:0;top:0;width:380px;height:310px;background:var(--photo-bottles)" role="img" aria-label="Foto: drei Flaschen Spätburgunder mit Weinkisten und Gläsern"></div>
    <svg class="curve" style="top:250px" width="380" height="70" viewBox="0 0 380 70" aria-hidden="true">
      <path d="M0 40Q200 70 380 0V70H0Z" fill="var(--paper)"/>
      <path d="M0 60Q220 80 380 14V22Q220 88 0 70Z" fill="var(--wine)"/>
    </svg>
    <div class="text-block" style="top:350px">
      <h2 class="heading" style="font-size:26px">Junge Weine</h2>
      <p class="subline">Weinverkauf nach Absprache</p>
      <p class="copy">Unsere Weine bekommen Sie direkt bei uns. Rufen Sie einfach an oder schreiben Sie uns, wir finden gern einen Termin für Probe und Abholung ganz nach Ihren Wünschen.</p>
      <p class="copy" style="margin-top:14px">Zum Verkauf stehen folgende Weine:</p>
      <ul class="wine-list">
        <li>Spätburgunder trocken 2016</li>
        <li>Blanc de Noir trocken 2017</li>
        <li>Blanc de Noir Sekt 2016</li>
      </ul>
    </div>
  </article>

  <article class="panel panel--wine">
    <h2 class="heading team-heading">Die Jungwinzer</h2>
    <div class="member" style="top:110px">
      <span class="round-photo" role="img" aria-label="Schwarzweiß-Porträt von Jonas Berger"></span>
      <p>Jonas Berger</p>
    </div>
    <div class="member" style="top:340px">
      <span class="round-photo" role="img" aria-label="Schwarzweiß-Porträt von Lukas Hellwig"></span>
      <p>Lukas Hellwig</p>
    </div>
    <div class="member" style="top:570px">
      <span class="round-photo" role="img" aria-label="Schwarzweiß-Foto von Moritz Anselm bei der Arbeit an der Rebe"></span>
      <p>Moritz Anselm</p>
    </div>
  </article>

  <article class="panel panel--light">
    <div class="bio" style="top:40px">
      <h3 class="heading">Jonas Berger</h3>
      <p class="copy">Jonas absolvierte seine Ausbildung zum Winzer von 2012 bis 2015 beim Weingut Hohlfeld. Von 2015 bis 2016 machte er sein Fachabitur für Agrarwirtschaft.</p>
      <p class="copy">Seitdem ist er als Winzer im Weingut Hohlfeld angestellt und sammelt wichtige Erfahrungen. Seit 2018 macht er nebenher die Ausbildung zum Winzermeister.</p>
      <p class="copy">Zum Weinbau ist er durch seinen Opa gekommen, der jahrzehntelang Reben gepflegt hat.</p>
    </div>
    <div class="bio" style="top:300px">
      <h3 class="heading">Lukas Hellwig</h3>
      <p class="copy">Lukas absolvierte seine Ausbildung zum Winzer von 2012 bis 2015 beim Weingut Sonnhang.</p>
      <p class="copy">Von 2015 bis 2016 machte er sein Fachabitur für Agrarwirtschaft. Seit Herbst 2016 studiert er Weinbau und Oenologie an der Hochschule.</p>
      <p class="copy">Weinbau wird in seiner Familie in der fünften Generation betrieben, so ist es naheliegend, dass er den elterlichen Betrieb übernimmt.</p>
    </div>
    <div class="bio" style="top:550px">
      <h3 class="heading">Moritz Anselm</h3>
      <p class="copy">Moritz absolvierte seine Ausbildung zum Winzer von 2012 bis 2015 beim Weingut Lindenhof und beim Rebentaler Winzerverein.</p>
      <p class="copy">Von 2015 bis 2016 machte er sein Fachabitur für Agrarwirtschaft. Seit Herbst 2016 studiert er Weinbau und Oenologie an der Hochschule.</p>
      <p class="copy">Zum Weinbau ist er durch seinen Onkel gekommen, der Kellermeister in einem großen Weingut ist.</p>
    </div>
  </article>
</section>

</body>
</html>
```